New Innovative Product needs a new business card design

We need a business card design for a new product line based in Michigan called "Lendwise Tailwind." We are a credit company by nature however this product should have a clean, simple, "zorvik-esque" feel. We have a few tag lines we use that could or could not be used...."All Referral Roads Lead to You" we use the attached pic in much or our marketing and also use both a white and/or black logo. Also attached.

We want the image attached on the card in some form or another- the grass/sky image.

Reason: We are extending to go over options with management- (expiring on weekend)

Reason: To finalize our design pick. We will be in touch with the designer of choice within the next day or so...the last few entries have been great- Sorry for the delay.

Reason: Working with a couple different designs trying to get finalized

Reason: Final in the workds

Marketing

• We want the image attached on the card in some form or another- the grass/sky image.

```html
<!DOCTYPE html>
<html lang="en">
<head>
<meta charset="utf-8">
<title>Lendwise Tailwind – Business Card</title>
<link href="https://fonts.googleapis.com/css2?family=Michroma&family=Roboto+Condensed:wght@400&display=swap" rel="stylesheet">
<style>
  :root {
    --bg: #e9e9e7;
    --card: #ffffff;
    --green: #1a9a4a;
    --green-dark: #127a39;
    --ink: #1d1d1d;
    --grey: #555555;
    --rule: #9a9a9a;
  }
  html, body {
    margin: 0;
    width: 1200px;
    height: 901px;
    overflow: hidden;
    background: var(--bg);
  }
  .card {
    position: absolute;
    left: 150px;
    top: 193px;
    width: 900px;
    height: 514px;
    background: var(--card);
    border-radius: 40px;
    overflow: hidden;
    box-shadow: 0 8px 28px rgba(0,0,0,0.18);
    font-family: "Michroma", sans-serif;
  }
  .brand {
    position: absolute;
    top: 70px;
    left: 0;
    width: 100%;
    display: flex;
    justify-content: center;
    align-items: center;
    gap: 14px;
  }
  .brand-mark {
    width: 34px;
    height: 34px;
    background: var(--green);
  }
  .brand-name {
    font-family: "Roboto Condensed", sans-serif;
    font-weight: 400;
    font-size: 46px;
    color: var(--ink);
    letter-spacing: -0.5px;
  }
  .identity {
    position: absolute;
    top: 178px;
    right: 490px;
    text-align: right;
  }
  .person-name {
    color: var(--green);
    font-size: 19px;
    letter-spacing: 3px;
    margin: 0 0 6px;
  }
  .person-role {
    color: var(--grey);
    font-size: 13px;
    letter-spacing: 2.5px;
    margin: 0 0 22px;
  }
  .address {
    color: var(--grey);
    font-size: 13px;
    letter-spacing: 2px;
    line-height: 26px;
    font-style: normal;
  }
  .divider {
    position: absolute;
    left: 430px;
    top: 172px;
    width: 1px;
    height: 140px;
    background: var(--rule);
  }
  .contacts {
    position: absolute;
    top: 176px;
    left: 452px;
    margin: 0;
    padding: 0;
    list-style: none;
  }
  .contacts li {
    display: flex;
    align-items: center;
    gap: 10px;
    height: 26px;
    color: var(--ink);
    font-size: 13px;
    letter-spacing: 2.5px;
  }
  .contacts svg { flex: none; }
  .band {
    position: absolute;
    left: 0;
    bottom: 0;
    width: 900px;
    height: 514px;
  }
  .web {
    position: absolute;
    left: 150px;
    top: 430px;
    color: #ffffff;
    font-size: 16px;
    letter-spacing: 3px;
    transform: rotate(8deg);
    transform-origin: left center;
  }
</style>
</head>
<body>
  <div class="card">
    <svg class="band" viewBox="0 0 900 514" aria-hidden="true">
      <path d="M0 332 C 250 350, 600 380, 900 505 L 900 514 L 0 514 Z" fill="#111111"/>
      <path d="M0 352 C 260 366, 610 400, 900 514 L 0 514 Z" fill="var(--green)"/>
    </svg>

    <div class="brand">
      <span class="brand-mark"></span>
      <span class="brand-name">Lendwise Tailwind</span>
    </div>

    <div class="identity">
      <p class="person-name">DANA WHITFORD</p>
      <p class="person-role">OWNER / C.E.O</p>
      <address class="address">SUITE # 214, ELM BLDG,<br>MI 48207</address>
    </div>

    <div class="divider"></div>

    <ul class="contacts">
      <li><svg width="16" height="16" viewBox="0 0 16 16"><circle cx="8" cy="8" r="8" fill="var(--green)"/><path d="M5 4.5 L6.5 4 L7.3 6 L6.4 6.8 Q7.3 8.7 9.2 9.6 L10 8.7 L12 9.5 L11.5 11 Q7 11 5 6.5 Z" fill="#fff"/></svg>555-210-4417</li>
      <li><svg width="16" height="16" viewBox="0 0 16 16"><circle cx="8" cy="8" r="8" fill="var(--green)"/><rect x="5.5" y="3.5" width="5" height="9" rx="1" fill="#fff"/></svg>555-302-8861</li>
      <li><svg width="16" height="16" viewBox="0 0 16 16"><circle cx="8" cy="8" r="8" fill="var(--green)"/><rect x="4" y="6" width="8" height="5" fill="#fff"/><rect x="5.5" y="4" width="5" height="2" fill="#fff"/></svg>555-418-2093</li>
      <li><svg width="16" height="16" viewBox="0 0 16 16"><circle cx="8" cy="8" r="8" fill="var(--green)"/><rect x="4" y="5" width="8" height="6" fill="#fff"/><path d="M4 5 L8 8.5 L12 5" stroke="var(--green)" fill="none"/></svg>dana@lendwisetailwind.com</li>
      <li><svg width="16" height="16" viewBox="0 0 16 16"><circle cx="8" cy="8" r="8" fill="var(--green)"/><circle cx="8" cy="8" r="4.5" fill="none" stroke="#fff"/><path d="M3.5 8 H12.5 M8 3.5 V12.5" stroke="#fff"/></svg>www.lendwisetailwind.com</li>
    </ul>

    <div class="web">WWW.LENDWISETAILWIND.COM</div>
  </div>
</body>
</html>
```